TrueHaven marketing postcards (6x9)

I would like to replicate this 6x9 postcard, but update name/logo, phone number, web address, etc. I also need to create a second postcard copying this basic design, but with updated content and background pictures. Updated contact info to be used for both postcards:
Website: www.truehavenhomes.example
Name: Mark Fellows
Email: mfellows@truehavenhomes.example
Phone: (555) 204-6139

Requirements
Must have
• Need two 6x9 postcard designs; 1 themed for Ridgemont State, 1 for Corvale Tech. Have uploaded photos that can be used in design. RS can be used for RS postcard (only), CT can be used for CT (only), Generic can be used for either. I've tried to upload extra photos so that you can use your creativity in selecting those that work best in the design.
Nice to have
• In the "Color palette" file, it has the two color schemes -- one for Ridgemont State and one for Corvale Tech. Those respective color schemes should be heavily represented in each design. Then there are different groups of pictures labelled either "CT" or "RS", plus some labelled "Generic". The generic ones can be used in either design, the others should be used only for the design for that school.

```html
<!DOCTYPE html>
<html lang="en">
<head>
<meta charset="utf-8">
<title>TrueHaven Postcards</title>
<link rel="stylesheet" href="https://fonts.googleapis.com/css2?family=Source+Sans+3:wght@400;600&family=Open+Sans:wght@700&family=Oswald:wght@500&display=swap">
<style>
:root{
  --page:#d9dadb;
  --dark:#1b1b1b;
  --dark-2:#3a3a3a;
  --orange:#e07020;
  --orange-cream:#f8e6d4;
  --maroon:#5a0026;
  --maroon-cream:#fbf3ec;
  --white:#ffffff;
  --ink:#1e1e1e;
  --muted:#7a6a5e;
}
*{box-sizing:border-box;margin:0;padding:0}
html,body{width:1200px;height:814px;overflow:hidden}
body{background:var(--page);font-family:"Source Sans 3",sans-serif;position:relative}
.card{position:absolute;width:510px;height:345px;overflow:hidden;box-shadow:2px 4px 8px rgba(0,0,0,.35)}
.card--rs{--accent:var(--orange);--cream:var(--orange-cream)}
.card--ct{--accent:var(--maroon);--cream:var(--maroon-cream)}
.pos-1{left:58px;top:61px}.pos-2{left:620px;top:61px}
.pos-3{left:58px;top:425px}.pos-4{left:620px;top:425px}
.dash{position:absolute;inset:7px;border:1px dashed rgba(255,255,255,.55);pointer-events:none;z-index:5}
.card--back .dash{border-color:rgba(0,0,0,.25)}
/* front */
.front{background:var(--dark)}
.front .topband{position:absolute;left:0;top:0;width:510px;height:52px;background:linear-gradient(180deg,#2b2b2b,#4a4a4a 60%,#222)}
.front .accent-line{position:absolute;left:182px;width:328px;height:4px;background:var(--accent)}
.front .photo{position:absolute;left:182px;top:56px;width:328px;height:238px}
.card--rs .photo{background:radial-gradient(ellipse at 55% 50%,#f2b441,#d98a1a 60%,#9a4e0c)}
.card--ct .photo{background:linear-gradient(180deg,#d98559 0%,#b45c4a 35%,#3a2c3a 65%,#141318 100%)}
.front .column{position:absolute;left:15px;top:0;width:167px;height:345px;background:var(--accent);color:var(--white);padding:0 0 0 9px}
.headline{font-weight:600;font-size:14.5px;line-height:20px;margin-top:52px}
.rule{width:50px;height:2px;background:var(--white);margin:10px 0 9px}
.card--rs .rule{background:var(--dark)}
.body{font-size:11px;line-height:13.8px;padding-right:4px}
.help{font-size:10px;margin:21px 0 0 16px}
.pill{display:flex;align-items:center;gap:10px;height:21px;width:139px;border-radius:11px;margin-top:7px;padding-left:16px;font-size:12px}
.card--rs .front-pill{background:var(--dark);color:var(--white)}
.card--ct .front-pill{background:var(--white);color:var(--dark)}
.pill svg{width:11px;height:11px}
.name{font-size:16px;margin:7px 0 0 28px;color:var(--white)}
.card--rs .name{color:#fde6cc}
.logo{position:absolute;right:18px;top:19px;display:flex;align-items:center;gap:6px;font-family:"Oswald",sans-serif;font-weight:500;font-size:12.5px;letter-spacing:.2px;text-transform:uppercase;color:var(--white)}
.logo .mark{width:14px;height:14px;background:currentColor}
.contacts{position:absolute;left:186px;right:14px;top:308px;display:flex;justify-content:space-between;color:var(--white);font-size:8.8px;font-weight:600;white-space:nowrap}
.contacts span{display:flex;align-items:center;gap:4px}
.dot{width:8px;height:8px;border-radius:50%;border:1.5px solid #bbb;flex:none}
/* back */
.back{background:var(--white)}
.back .panel{position:absolute;left:0;top:0;width:260px;height:345px;background:var(--cream)}
.back .ph-a{position:absolute;left:0;top:0;width:97px;height:96px;background:linear-gradient(180deg,#c9ccd1,#7f93ab)}
.back .ph-b{position:absolute;left:97px;top:0;width:158px;height:96px}
.card--rs .ph-b{background:linear-gradient(180deg,#9ab6cf 0%,#6d7f5a 40%,#314d63 100%)}
.card--ct .ph-b{background:linear-gradient(180deg,#5d8fc9 0%,#c9c4b4 45%,#9d917d 100%)}
.back .banner{position:absolute;left:0;top:96px;width:260px;height:75px;background:var(--accent);color:#fbe6d6;font-family:"Open Sans",sans-serif;font-weight:700;font-size:16px;line-height:18px;padding:10px 0 0 24px;box-shadow:0 3px 5px rgba(0,0,0,.25)}
.back .copy{position:absolute;left:24px;top:187px;width:225px}
.back .lead{font-size:12px;line-height:17px;color:var(--ink)}
.back .rule{background:var(--dark);width:72px;margin:9px 0 8px;height:2px}
.back .note{font-size:9.5px;line-height:11.5px;color:var(--muted);font-weight:600}
.back .line{display:flex;align-items:center;gap:6px;font-size:8px;margin-top:14px;color:var(--ink);white-space:nowrap}
.back .line b{font-weight:600}
.back .bottom{position:absolute;left:0;top:302px;width:255px;height:43px;background:linear-gradient(180deg,#111,#2e2e2e);color:var(--white);font-size:9.5px;font-weight:600;text-align:center;padding-top:16px}
.back .cta{position:absolute;left:28px;top:294px;width:214px;height:20px;border-radius:10px;background:var(--accent);color:var(--white);display:flex;align-items:center;justify-content:center;gap:8px;font-size:13px;z-index:2}
.back .cta svg{width:11px;height:11px}
.back .logo{left:278px;right:auto;top:37px;color:var(--dark)}
.stamp{position:absolute;left:426px;top:25px;width:64px;height:59px;border:1px solid #e4e4e4}
</style>
</head>
<body>

<svg width="0" height="0" style="position:absolute">
  <symbol id="phone" viewBox="0 0 12 12"><circle cx="6" cy="6" r="5.3" fill="none" stroke="currentColor" stroke-width="1"/><path d="M4 3.3l1 .1.5 1.3-.7.6a4 4 0 0 0 1.9 1.9l.6-.7 1.3.5.1 1-.8.7C5.8 8.5 3.5 6.2 3.3 4.1z" fill="currentColor"/></symbol>
</svg>

<article class="card card--rs front pos-1">
  <div class="topband"></div>
  <div class="accent-line" style="top:52px"></div>
  <div class="photo" role="img" aria-label="Aged map of the United States with Texas highlighted in flag colours"></div>
  <div class="accent-line" style="top:294px"></div>
  <div class="logo"><span class="mark"></span>TrueHaven Residential</div>
  <div class="column">
    <h2 class="headline">Ridgehawk Families,<br>What would you do<br>with an extra $80,000?</h2>
    <div class="rule"></div>
    <p class="body">The professionals at TrueHaven Residential are passionate about helping out-of-state families establish Texas residency and qualify for in-state tuition. Saving your family more than $13,700 per semester.</p>
    <p class="help">LET US HELP YOU TOO.</p>
    <div class="pill front-pill"><svg><use href="#phone"/></svg>(555) 204-6139</div>
    <p class="name">Mark Fellows</p>
  </div>
  <div class="contacts"><span><i class="dot"></i>mfellows@truehavenhomes.example</span><span><i class="dot"></i>www.truehavenhomes.example</span></div>
  <div class="dash"></div>
</article>

<article class="card card--ct front pos-2">
  <div class="topband"></div>
  <div class="accent-line" style="top:52px"></div>
  <div class="photo" role="img" aria-label="Campus clock tower lit at dusk with city lights behind"></div>
  <div class="accent-line" style="top:294px"></div>
  <div class="logo"><span class="mark"></span>TrueHaven Residential</div>
  <div class="column">
    <h2 class="headline">Corvale Families,<br>What would you do<br>with an extra $79,000?</h2>
    <div class="rule"></div>
    <p class="body">The professionals at TrueHaven Residential are passionate about helping out-of-state families establish Texas residency and qualify for in-state tuition. Saving your family more than $13,200 per semester.</p>
    <p class="help">LET US HELP YOU TOO.</p>
    <div class="pill front-pill"><svg><use href="#phone"/></svg>(555) 204-6139</div>
    <p class="name">Mark Fellows</p>
  </div>
  <div class="contacts"><span><i class="dot"></i>mfellows@truehavenhomes.example</span><span><i class="dot"></i>www.truehavenhomes.example</span></div>
  <div class="dash"></div>
</article>

<article class="card card--rs back pos-3">
  <div class="panel"></div>
  <div class="ph-a" role="img" aria-label="Student with backpack holding books"></div>
  <div class="ph-b" role="img" aria-label="Arched bridge over a river among green hills"></div>
  <h2 class="banner">Let us help you save tens<br>of thousands of dollars<br>on tuition in Texas.</h2>
  <div class="copy">
    <p class="lead">Establishing Texas residency through a property purchase is as easy as 1-2-3.</p>
    <div class="rule"></div>
    <p class="note">Contact us now to learn how TrueHaven Residential is ready to become your trusted partner.</p>
    <p class="line">Let us help you too. <i class="dot"></i><b>mfellows@truehavenhomes.example</b></p>
  </div>
  <div class="bottom">www.truehavenhomes.example</div>
  <div class="cta">Mark Fellows <svg><use href="#phone"/></svg> (555) 204-6139</div>
  <div class="logo"><span class="mark"></span>TrueHaven Residential</div>
  <div class="stamp"></div>
  <div class="dash"></div>
</article>

<article class="card card--ct back pos-4">
  <div class="panel"></div>
  <div class="ph-a" role="img" aria-label="Student with backpack holding books"></div>
  <div class="ph-b" role="img" aria-label="Town water tower against a blue sky"></div>
  <h2 class="banner">Let us help you save tens<br>of thousands of dollars<br>on tuition in Texas.</h2>
  <div class="copy">
    <p class="lead">Establishing Texas residency through a property purchase is as easy as 1-2-3.</p>
    <div class="rule"></div>
    <p class="note">Contact us now to learn how TrueHaven Residential is ready to become your trusted partner.</p>
    <p class="line">Let us help you too. <i class="dot"></i><b>mfellows@truehavenhomes.example</b></p>
  </div>
  <div class="bottom">www.truehavenhomes.example</div>
  <div class="cta">Mark Fellows <svg><use href="#phone"/></svg> (555) 204-6139</div>
  <div class="logo"><span class="mark"></span>TrueHaven Residential</div>
  <div class="stamp"></div>
  <div class="dash"></div>
</article>

</body>
</html>
```